Nine Quiet Hours
Business Cards & Letterhead for Sleep Therapist - Health
Business Cards & Letterhead for Sleep Therapist
Professional
Nola J. Barnes, MA, RPSGT, RST, RCC
Founder - Sleep Therapist
4862 Fenwick Avenue, Suite 214 Toronto, ON M6P 2K8
855.52Hushh (855.527.3381)
nola@ninequiethours.example
www.ninequiethours.example www.nineq-hours.example
Front of card should be logo with the tagline "Sleep Consultants and Coaching" on mainly white background, and contact information as provided. I have a few versions of my logo -- I'd like to see both mocked up.
Dark background (black, navy or midnight blue) logo with the tagline "bright ideas for better sleep" & web addresses
jlbarnes jlbarnes
Sincerely, thank you to all the designers who submitted to my project ... I am so pleased with the quality of work.
Hello Designers, I'd appreciate not seeing full stationary design submissions until a business card layout you have submitted has been narrowed to a finalist. There are so many great and unique designs to review ... your time and mine is valuable. So, I will request to see the stationary package options from you when I have selected a business card design of yours that is remaining as one of my finalists. thank you!
Great start! Wow. Thank you for the submissions so far ... general feedback for now, with private feedback to follow soon: 1) please don't merge the two logo concepts (with rare exception - if you have stars on a design now that did this, you've done a unique job that somehow is working for me) The light blue sheep with white and black is one complete look. The yellow moon-bulb with white and midnight blue/navy or black is another complete look. I hope to see/have these two versions of the winning design layout. 2) the light blue as a full colour background for the back of the card doesn't work. I prefer black background with the sheep design on the back of the card. 3) do not use the Hushh for the toll free phone number just the numbers 855.527.3381 and please be sure to denote this as 'toll free' or TF. 4) please make sure both web addresses appear on the card ... if one is used on the front, the other must appear on the back. Or both can appear on the back only ... but both must appear. 5) both logo designs need the tagline "Sleep Coach and Consulting" (no quotation marks though) on the front of the card ... and "bright ideas for better sleep" (all lower case, no quotation marks) on the back of the card. Cheers! I'll do a fresh round of star ratings shortly
I'm open to creative interpretation of my directions ... ie. Logo on the back can be just an element of same (moon-bulb, sheep), larger watermark, etc.? The tagline does not have to reside just under the logo ... Although the front of the cards should be light background & back dark background I don't mind some of the creative touches that tie the sides together more artistically. You're the pros, so I look forward to seeing what is submitted!

```html
<!DOCTYPE html>
<html lang="en">
<head>
<meta charset="utf-8">
<title>Nine Quiet Hours – Business Card</title>
<link rel="stylesheet" href="https://fonts.googleapis.com/css2?family=Jost:wght@400;500;600&display=swap">
<style>
  :root {
    --page: #e9e6e1;
    --card-dark: #0b0b0b;
    --card-light: #ffffff;
    --teal: #8fd3d3;
    --teal-deep: #5bb8b8;
    --ink: #2b2b2b;
    --ink-soft: #4a4a4a;
    --white: #ffffff;
    --sheep-dark: #3a3a3a;
  }
  * { box-sizing: border-box; margin: 0; padding: 0; }
  html, body { width: 1200px; height: 904px; overflow: hidden; }
  body {
    background: var(--page);
    font-family: "Jost", "Futura", sans-serif;
    position: relative;
  }
  .card {
    position: absolute;
    width: 640px;
    height: 366px;
    border-radius: 22px;
    overflow: hidden;
    box-shadow: 0 6px 18px rgba(0,0,0,.18);
  }
  /* Back */
  .card-back { left: 80px; top: 64px; background: var(--card-dark); }
  .back-emblem {
    position: absolute; left: 258px; top: 72px;
    width: 124px; height: 124px; border-radius: 50%;
    background: radial-gradient(circle at 50% 45%, #ffffff 0 30%, var(--teal) 31%);
  }
  .back-tagline {
    position: absolute; left: 0; right: 0; top: 226px;
    text-align: center; color: var(--white);
    font-size: 14px; letter-spacing: .5px;
  }
  /* Front */
  .card-front { left: 480px; top: 474px; background: var(--card-light); }
  .logo { position: absolute; left: 34px; top: 44px; display: flex; align-items: center; gap: 10px; }
  .logo-dot { width: 16px; height: 16px; border-radius: 50%; background: var(--teal-deep); }
  .logo-name { font-size: 34px; font-weight: 600; color: var(--ink); line-height: 1; }
  .logo-tagline {
    position: absolute; left: 60px; top: 86px;
    font-size: 15px; color: var(--teal-deep); letter-spacing: .3px;
  }
  .band {
    position: absolute; left: 0; right: 0; top: 140px; height: 66px;
    background: var(--teal);
  }
  .address {
    position: absolute; left: 34px; top: 152px;
    font-size: 13px; line-height: 1.35; color: var(--ink);
  }
  .person { position: absolute; left: 250px; top: 150px; color: var(--ink); }
  .person-name { font-size: 20px; font-weight: 500; }
  .person-name .creds { font-size: 12px; font-weight: 400; letter-spacing: .3px; }
  .person-role { font-size: 13px; color: var(--white); margin-top: 2px; }
  .web-alt {
    position: absolute; right: 30px; top: 178px;
    font-size: 13px; color: var(--ink);
  }
  .front-emblem {
    position: absolute; right: 18px; top: 54px;
    width: 116px; height: 116px; border-radius: 50%;
    background: radial-gradient(circle at 50% 45%, var(--sheep-dark) 0 30%, var(--teal) 31%);
    border: 4px solid var(--white);
  }
  .contacts {
    position: absolute; left: 34px; top: 222px;
    list-style: none; font-size: 13px; color: var(--ink-soft);
  }
  .contacts li { display: flex; align-items: center; gap: 10px; height: 20px; }
  .contacts svg { width: 14px; height: 14px; fill: var(--ink-soft); }
  .contacts .label { font-size: 10px; color: var(--teal-deep); font-weight: 600; }
  .web-main {
    position: absolute; left: 34px; bottom: 18px;
    font-size: 13px; color: var(--ink);
  }
  .bottom-rule {
    position: absolute; left: 0; right: 0; bottom: 0; height: 8px; background: var(--teal);
  }
</style>
</head>
<body>
  <section class="card card-back">
    <div class="back-emblem" role="img" aria-label="Illustration of a sleeping white sheep on a scalloped light-blue circle"></div>
    <p class="back-tagline">bright ideas for better sleep</p>
  </section>

  <section class="card card-front">
    <div class="logo">
      <span class="logo-dot"></span>
      <span class="logo-name">Nine Quiet Hours</span>
    </div>
    <p class="logo-tagline">Sleep Consultants and Coaching</p>

    <div class="band"></div>
    <div class="front-emblem" role="img" aria-label="Illustration of a sleeping dark sheep on a scalloped light-blue circle"></div>

    <p class="address">4862 Fenwick Avenue, Suite 214<br>Toronto, ON M6P 2K8</p>
    <div class="person">
      <p class="person-name">Nola J. Barnes <span class="creds">MA RPSGT RST RCC</span></p>
      <p class="person-role">Founder - Sleep Therapist</p>
    </div>
    <p class="web-alt">www.nineq-hours.example</p>

    <ul class="contacts">
      <li><svg viewBox="0 0 24 24"><path d="M6.6 10.8a15 15 0 006.6 6.6l2.2-2.2c.3-.3.7-.4 1-.2 1.1.4 2.3.6 3.6.6.6 0 1 .4 1 1V20c0 .6-.4 1-1 1A17 17 0 013 4c0-.6.4-1 1-1h3.5c.6 0 1 .4 1 1 0 1.3.2 2.5.6 3.6.1.3 0 .7-.2 1z"/></svg><span class="label">TF</span>855.527.3381</li>
      <li><svg viewBox="0 0 24 24"><path d="M6.6 10.8a15 15 0 006.6 6.6l2.2-2.2c.3-.3.7-.4 1-.2 1.1.4 2.3.6 3.6.6.6 0 1 .4 1 1V20c0 .6-.4 1-1 1A17 17 0 013 4c0-.6.4-1 1-1h3.5c.6 0 1 .4 1 1 0 1.3.2 2.5.6 3.6.1.3 0 .7-.2 1z"/></svg>905.318.4470</li>
      <li><svg viewBox="0 0 24 24"><path d="M7 3h10v5H7zM4 9h16a1 1 0 011 1v8h-4v3H7v-3H3v-8a1 1 0 011-1zm5 7v3h6v-3z"/></svg>888.206.7153</li>
      <li><svg viewBox="0 0 24 24"><path d="M3 5h18a1 1 0 011 1v12a1 1 0 01-1 1H3a1 1 0 01-1-1V6a1 1 0 011-1zm1 2.2V17h16V7.2l-8 5.3z"/></svg>nola@ninequiethours.example</li>
    </ul>

    <p class="web-main">www.ninequiethours.example</p>
    <div class="bottom-rule"></div>
  </section>
</body>
</html>
```